Elegant wine label

Looking for a new Napa Valley wine label called "Velmora". Our wines will retail for $150 + per bottle. Velmora is derived from the greek word Ergo (therefore) tied in with Air for aeration for wine.

We handcraft our small production wine. 200 cases.
Looking for a very sophisticated, minimalist elegant look. Wine labels we like for inspiration and reference include: www.tarvik.wine, www.pellunwine.com, www.morvadestates.com, www.quillbarrowwine.com, www.brevixestate.com/Wine, https://shop.lantivewine.com/wine

Colors will include white, black and blue foil (Approx. color: C 94.9, M 83.53, Y 0, K 0). We want a custom-created, minimal greek/roman looking font for lettering.

```html
<!DOCTYPE html>
<html lang="en">
<head>
<meta charset="UTF-8">
<title>Velmora — Napa Valley Label</title>
<link rel="stylesheet" href="https://fonts.googleapis.com/css2?family=Cinzel:wght@400&family=Cormorant+Garamond:ital,wght@1,500&family=Montserrat:wght@600&display=swap">
<style>
  :root {
    --backdrop: #2b2e2f;
    --label-paper: #f6f5ef;
    --label-edge: #e9e7dd;
    --ink-black: #1b1b1b;
    --ink-grey: #7a7a7a;
    --foil-blue-light: #4f8fe6;
    --foil-blue: #2a52d6;
    --foil-blue-deep: #2330b0;
  }
  * { box-sizing: border-box; margin: 0; padding: 0; }
  html, body {
    width: 668px;
    height: 1200px;
    overflow: hidden;
    background: var(--backdrop);
  }
  .canvas {
    position: relative;
    width: 668px;
    height: 1200px;
    display: flex;
    align-items: center;
    justify-content: center;
  }
  .label {
    position: relative;
    width: 560px;
    height: 590px;
    background: linear-gradient(90deg, var(--label-paper) 0%, #fbfbf8 45%, var(--label-edge) 100%);
  }
  .label__emblem {
    position: absolute;
    left: 200px;
    top: 62px;
    width: 160px;
    height: 290px;
    background: linear-gradient(160deg, var(--foil-blue-light) 0%, var(--foil-blue) 55%, var(--foil-blue-deep) 100%);
    opacity: 0.85;
  }
  .label__vintage {
    position: absolute;
    top: 360px;
    left: 0;
    width: 100%;
    text-align: center;
    font-family: "Cormorant Garamond", serif;
    font-style: italic;
    font-weight: 500;
    font-size: 25px;
    line-height: 1;
    letter-spacing: 4px;
    color: var(--ink-black);
  }
  .label__name {
    position: absolute;
    top: 392px;
    left: 0;
    width: 100%;
    text-align: center;
    font-family: "Cinzel", serif;
    font-weight: 400;
    font-size: 84px;
    line-height: 1;
    letter-spacing: 1px;
    color: var(--ink-black);
  }
  .label__region {
    position: absolute;
    top: 528px;
    left: 0;
    width: 100%;
    text-align: center;
    font-family: "Montserrat", sans-serif;
    font-weight: 600;
    font-size: 16px;
    line-height: 1;
    letter-spacing: 2px;
    color: var(--ink-black);
  }
  .label__region-first { color: var(--ink-grey); }
</style>
</head>
<body>
  <main class="canvas">
    <section class="label">
      <div class="label__emblem" role="img" aria-label="Blue foil engraved emblem of a classical wind figure blowing air"></div>
      <p class="label__vintage">2024</p>
      <h1 class="label__name">Velmora</h1>
      <p class="label__region"><span class="label__region-first">NAPA</span> VALLEY</p>
    </section>
  </main>
</body>
</html>
```